Ridgeway Spectral Studies Website

We are a paranormal research group located in Central Mississippi. We are a group dedicated to help the community in any paranormal investigation. We use fresh new techniques with cutting edge technology to investigate any paranormal situation. Our services are always free of charge to anyone. An unique feature of our group is that we provide a complete history of the property, courtesy of our research team. We would like to see designs that incorporate our logo. We are a professional group and want a professional website.. we will need a home page that will reflect out goals. Links will include "Home, About Us, Contact us, (MAYBE MORE). We will also want a "blank page" with same links that we can edit and fill in all the information..

Target Market(s)

Paranormal-Ghost hunting groups

Industry/Entity Type

Community

Coding

Coded - Design and coding required

Number of Pages Required

2 page

Font styles to use
Other font styles liked:

Requirements
Must have
• we will need a home page that will reflect out goals. Links will include "Home, About Us, Contact us, (MAYBE MORE). We will also want a "blank page" with same links that we can edit and fill in all the information..

```html
<!DOCTYPE html>
<html lang="en">
<head>
<meta charset="utf-8">
<title>Ridgeway Spectral Studies</title>
<link rel="stylesheet" href="https://fonts.googleapis.com/css2?family=Poppins:wght@700;800&family=Arimo:wght@400&family=Signika:wght@700&display=swap">
<style>
  :root {
    --ink: #000000;
    --paper: #ffffff;
    --rule: #d8d8d8;
    --muted: #bbbbbb;
    --fog-light: #8c8c84;
    --fog-mid: #3e3f3a;
    --forest-dark: #121312;
  }
  * { margin: 0; padding: 0; box-sizing: border-box; }
  html, body { width: 1200px; height: 588px; overflow: hidden; background: var(--ink); }
  .page { position: relative; width: 1200px; height: 588px; overflow: hidden; color: var(--paper); }

  .hero-scene {
    position: absolute; inset: 0;
    background:
      radial-gradient(ellipse 260px 330px at 700px 170px, var(--fog-light) 0%, #6a6b64 30%, transparent 75%),
      radial-gradient(ellipse 520px 420px at 650px 300px, var(--fog-mid) 0%, transparent 80%),
      linear-gradient(90deg, #0b0c0b 0%, var(--forest-dark) 25%, #232421 50%, var(--forest-dark) 75%, #0b0c0b 100%);
  }

  .site-header { position: absolute; top: 0; left: 0; width: 1200px; height: 65px; background: var(--ink); }
  .site-header::before, .site-header::after {
    content: ""; position: absolute; left: 0; width: 1200px; height: 1px; background: var(--rule);
  }
  .site-header::before { top: 33px; }
  .site-header::after { top: 64px; }

  .main-nav a {
    position: absolute; top: 39px;
    font-family: "Signika", sans-serif; font-weight: 700; font-size: 12px;
    color: var(--paper); text-decoration: none; white-space: nowrap;
  }

  .brand {
    position: absolute; left: 545px; top: 4px; width: 94px; height: 94px;
    background: var(--ink); border: 1px solid var(--rule);
    display: flex; align-items: center; justify-content: center; text-align: center;
    font-family: "Signika", sans-serif; font-weight: 700; font-size: 12px; line-height: 1.2;
    color: var(--paper); padding: 6px;
  }

  .intro { position: absolute; left: 42px; top: 210px; width: 330px; }
  .intro-title {
    font-family: "Poppins", sans-serif; font-weight: 800; font-size: 47px;
    line-height: 52px; letter-spacing: -2.5px; white-space: nowrap;
  }
  .intro-text {
    margin-top: 14px; width: 311px;
    font-family: "Arimo", sans-serif; font-size: 15px; line-height: 16.5px;
    letter-spacing: 1.5px;
  }
  .intro-line { display: block; white-space: nowrap; text-align: justify; text-align-last: justify; }
  .intro-line-last { text-align-last: left; }

  .side-links { position: absolute; left: 1000px; top: 228px; width: 160px; }
  .side-link { display: flex; align-items: center; gap: 4px; font-family: "Poppins", sans-serif; font-weight: 700; }
  .side-link-small { font-size: 19px; line-height: 24px; }
  .side-feature { margin-top: 24px; position: relative; }
  .side-feature-icon { position: absolute; left: 2px; top: -2px; }
  .side-feature-title {
    padding-left: 14px; font-family: "Poppins", sans-serif; font-weight: 700;
    font-size: 31px; line-height: 34px; padding-top: 6px;
  }
  .side-feature-meta {
    display: flex; justify-content: space-between; align-items: center;
    margin-top: 8px; padding-left: 16px; width: 146px;
    font-family: "Poppins", sans-serif; font-weight: 800; font-size: 10px;
    font-variant: small-caps; letter-spacing: 0.3px;
  }
  .side-feature-chevron { flex: none; }
</style>
</head>
<body>
<div class="page">
  <div class="hero-scene" role="img" aria-label="Dark misty forest with a winding road fading into fog"></div>

  <header class="site-header">
    <nav class="main-nav">
      <a href="#" style="left:330px">Home</a>
      <a href="#" style="left:390px">About us</a>
      <a href="#" style="left:467px">Services</a>
      <a href="#" style="left:668px">How it works</a>
      <a href="#" style="left:768px">Feedback</a>
      <a href="#" style="left:848px">Contact us</a>
    </nav>
  </header>

  <div class="brand">Ridgeway Spectral Studies</div>

  <section class="intro">
    <h1 class="intro-title">What is Lorem<br>Ipsum?</h1>
    <p class="intro-text">
      <span class="intro-line">Lorem Ipsum is simply dummy text</span>
      <span class="intro-line">of the printing and typesetting in-</span>
      <span class="intro-line">dustry. Lorem Ipsum has been the</span>
      <span class="intro-line">industry's standard dummy text</span>
      <span class="intro-line intro-line-last">ever since the 1500s.</span>
    </p>
  </section>

  <aside class="side-links">
    <div class="side-link side-link-small">
      <svg width="16" height="16" viewBox="0 0 16 16"><circle cx="8" cy="8" r="7" fill="none" stroke="#fff" stroke-width="2"/><path d="M6 4.5 L10 8 L6 11.5" fill="none" stroke="#fff" stroke-width="2.2"/></svg>
      <span>Lorem Ipsum</span>
    </div>
    <div class="side-feature">
      <svg class="side-feature-icon" width="16" height="16" viewBox="0 0 16 16"><circle cx="8" cy="8" r="7" fill="none" stroke="#fff" stroke-width="2"/><path d="M6 4.5 L10 8 L6 11.5" fill="none" stroke="#fff" stroke-width="2.2"/></svg>
      <h2 class="side-feature-title">Lorem<br>Ipsum</h2>
      <div class="side-feature-meta">
        <span>Lorem Ipsum</span>
        <svg class="side-feature-chevron" width="12" height="8" viewBox="0 0 12 8"><path d="M1.5 1.5 L6 6 L10.5 1.5" fill="none" stroke="#bbbbbb" stroke-width="2"/></svg>
      </div>
    </div>
  </aside>
</div>
</body>
</html>
```